Business Card Design for Marketing Firm

Looking for business card design for higher end marketing firm. Clean but impressionable/trendy. We are a marketing firm that represents manufacturers in the foodservice equipment and supply industry. Our customers are end users such has hotels, restaurants, country clubs, convention centers and casinos as well as distributors of restaurants supplies and equipment, and manufacturers of foodservice equipment and supplies.
Target Market(s)
Hotels, Restaurants, Supply & Equipment Distributors, Foodservice Manufacturers
Industry/Entity Type
Foodservice/Hospitality
Contact Information for Business Card
Name, Title, Contact Number, Email, Website, Social Media, Address
Requirements
Must have
- Clean & Simple but Serious and Impressionable

```html
<!DOCTYPE html>
<html lang="en">
<head>
<meta charset="utf-8">
<title>Meridian Service Reps – Business Card</title>
<link rel="stylesheet" href="https://fonts.googleapis.com/css2?family=Open+Sans:wght@400;700&display=swap">
<style>
  :root {
    --backdrop: #222222;
    --card-white: #ffffff;
    --brand-navy: #2b2a7d;
    --brand-blue: #2e2c86;
    --ink: #1a1a1a;
    --rule: #2a2a2a;
    --dot-a: #e4405f;
    --dot-b: #2d5fb5;
    --dot-c: #2ba3e8;
    --dot-d: #d92d2d;
  }
  * { margin: 0; padding: 0; box-sizing: border-box; }
  html, body { width: 1200px; height: 780px; overflow: hidden; }
  body {
    background: var(--backdrop);
    font-family: "Open Sans", Arial, sans-serif;
    position: relative;
  }
  .card {
    position: absolute;
    top: 240px;
    width: 525px;
    height: 300px;
    border-radius: 2px;
    box-shadow: 0 14px 30px rgba(0,0,0,.45);
  }
  .card--front { left: 50px; background: var(--card-white); }
  .card--back  { left: 625px; background: var(--brand-blue); }

  .brand {
    position: absolute;
    display: flex;
    align-items: center;
    gap: 10px;
    font-weight: 700;
    letter-spacing: .04em;
    text-transform: uppercase;
    line-height: 1.15;
  }
  .brand__mark { flex: none; border-radius: 50%; }
  .card--front .brand {
    left: 30px; top: 70px; width: 220px;
    color: var(--brand-navy); font-size: 17px;
  }
  .card--front .brand__mark { width: 18px; height: 18px; background: var(--brand-navy); }
  .card--back .brand {
    left: 0; right: 0; top: 0; bottom: 0; justify-content: center;
    color: #3a3a99; font-size: 26px;
    text-shadow: none;
  }
  .card--back .brand__mark { width: 24px; height: 24px; background: #3a3a99; }

  .social {
    position: absolute; left: 78px; top: 210px;
    display: flex; gap: 9px; list-style: none;
  }
  .social__dot { width: 15px; height: 15px; border-radius: 50%; }
  .social__dot--1 { background: var(--dot-a); }
  .social__dot--2 { background: var(--dot-b); }
  .social__dot--3 { background: var(--dot-c); }
  .social__dot--4 { background: var(--dot-d); }

  .divider { position: absolute; left: 230px; top: 70px; }

  .contact {
    position: absolute; left: 290px; top: 64px; right: 18px;
    color: var(--ink);
  }
  .contact__name {
    color: var(--brand-navy); font-weight: 700; font-size: 25px; line-height: 1.1;
  }
  .contact__title { font-size: 13px; margin-bottom: 10px; }
  .contact__address { font-size: 13px; line-height: 1.35; margin-bottom: 4px; font-style: normal; }
  .contact__list { list-style: none; font-size: 13px; line-height: 1.5; }
  .contact__item { display: flex; align-items: center; gap: 7px; }
  .contact__icon { width: 11px; height: 11px; flex: none; fill: var(--brand-navy); }
</style>
</head>
<body>

<section class="card card--front" aria-label="Business card front">
  <div class="brand">
    <span class="brand__mark"></span>
    <span class="brand__name">Meridian Service Reps</span>
  </div>

  <ul class="social" aria-label="Social media">
    <li class="social__dot social__dot--1" role="img" aria-label="Social profile"></li>
    <li class="social__dot social__dot--2" role="img" aria-label="Social profile"></li>
    <li class="social__dot social__dot--3" role="img" aria-label="Social profile"></li>
    <li class="social__dot social__dot--4" role="img" aria-label="Social profile"></li>
  </ul>

  <svg class="divider" width="40" height="170" viewBox="0 0 40 170" aria-hidden="true">
    <line x1="38" y1="0" x2="2" y2="170" stroke="var(--rule)" stroke-width="1"/>
  </svg>

  <div class="contact">
    <h1 class="contact__name">Graham Ellison</h1>
    <p class="contact__title">Executive Leader</p>
    <address class="contact__address">Headquarters<br>Dallas, Texas US</address>
    <ul class="contact__list">
      <li class="contact__item">
        <svg class="contact__icon" viewBox="0 0 24 24" aria-hidden="true"><path d="M6.6 10.8a15 15 0 0 0 6.6 6.6l2.2-2.2a1 1 0 0 1 1-.25 11.4 11.4 0 0 0 3.6.57 1 1 0 0 1 1 1V20a1 1 0 0 1-1 1A17 17 0 0 1 3 4a1 1 0 0 1 1-1h3.5a1 1 0 0 1 1 1c0 1.25.2 2.45.57 3.6a1 1 0 0 1-.25 1z"/></svg>
        (555) 014 2730
      </li>
      <li class="contact__item">
        <svg class="contact__icon" viewBox="0 0 24 24" aria-hidden="true"><circle cx="12" cy="12" r="10" fill="none" stroke="var(--brand-navy)" stroke-width="2.4"/><path d="M2 12h20M12 2c3 3 3 17 0 20M12 2c-3 3-3 17 0 20" fill="none" stroke="var(--brand-navy)" stroke-width="1.8"/></svg>
        www.meridianservicereps.com
      </li>
      <li class="contact__item">
        <svg class="contact__icon" viewBox="0 0 24 24" aria-hidden="true"><path d="M2 5h20v14H2z M2 5l10 8 10-8" fill="none" stroke="var(--brand-navy)" stroke-width="2.4"/></svg>
        hello@meridianservicereps.com
      </li>
    </ul>
  </div>
</section>

<section class="card card--back" aria-label="Business card back">
  <div class="brand">
    <span class="brand__mark"></span>
    <span class="brand__name">Meridian Service Reps</span>
  </div>
</section>

</body>
</html>
```